Menu for Coffee Shop / Restaurant

we are looking for someone to redesign our menus. would like something clean and modern, not too over the top. The business is a coffee shop during the day and transitions to a bar/restaurant in the evenings, so we need a design versatile enough to be used on everything from breakfast menus to cocktail menus. i've attached logo files as well as the current menu files. We're looking to do one menu each for breakfast, brunch (served only on weekends), one that combines the items listed on the attached lunch and dinner menus, and a dessert menu.

Industry/Entity Type

Business

Colors

Designer to choose colors to be used in the design.

Requirements
Must have
• 4 menus : breakfast, brunch, regular food service (combine lunch and dinner menus) and a dessert menu
Nice to have
• would prefer that each menu fit on 1 page, not double sided. We're ok with using legal size paper in order to accomodate

```html
<!DOCTYPE html>
<html lang="en">
<head>
<meta charset="utf-8">
<title>Kettlewell Breakfast Menu</title>
<link rel="stylesheet" href="https://fonts.googleapis.com/css2?family=Oswald:wght@500&family=Josefin+Sans:wght@600;700&family=Lato:wght@400;700&display=swap">
<style>
  :root {
    --backdrop: #1f1f1f;
    --paper: #ffffff;
    --sky: #5cc8e8;
    --ink: #141414;
    --ink-soft: #2b2b2b;
  }
  * { box-sizing: border-box; margin: 0; padding: 0; }
  html, body { width: 1200px; height: 3180px; overflow: hidden; }
  body {
    background: var(--backdrop);
    position: relative;
    font-family: "Lato", Arial, sans-serif;
    color: var(--ink);
  }
  .page {
    position: absolute;
    left: 191px;
    width: 829px;
    height: 1155px;
    background: var(--paper);
  }
  .page--cover { top: 314px; }
  .page--menu { top: 1791px; }

  .cover-mark {
    position: absolute;
    left: 0; right: 0; top: 540px;
    display: flex; align-items: center; justify-content: center; gap: 18px;
    font-family: "Oswald", sans-serif;
    font-weight: 500;
    font-size: 64px;
    letter-spacing: 10px;
    color: var(--sky);
  }
  .cover-mark .dot { width: 22px; height: 22px; border-radius: 50%; background: var(--sky); }

  .masthead { position: absolute; left: 95px; top: 52px; }
  .masthead__name {
    font-family: "Oswald", sans-serif; font-weight: 500;
    font-size: 62px; line-height: 1; letter-spacing: 14px; color: var(--sky);
  }
  .masthead__section {
    margin-top: 18px;
    font-family: "Josefin Sans", sans-serif; font-weight: 700;
    font-size: 22px; letter-spacing: 8px; color: var(--ink);
  }

  .builder {
    position: absolute; left: 47px; top: 208px; width: 736px; height: 312px;
    background: var(--sky);
  }
  .builder__title {
    position: absolute; left: 0; right: 0; top: 22px; text-align: center;
    font-family: "Josefin Sans", sans-serif; font-weight: 700;
    font-size: 21px; letter-spacing: 2px;
  }
  .rule { display: block; width: 66px; height: 3px; background: var(--ink); }
  .builder__title .rule { margin: 12px auto 0; }
  .builder__col { position: absolute; top: 92px; }
  .builder__col--bread { left: 30px; width: 260px; }
  .builder__col--cheese { left: 314px; width: 200px; }
  .builder__col--protein { left: 524px; width: 190px; }
  .col-head {
    display: flex; justify-content: space-between; align-items: baseline;
    font-family: "Josefin Sans", sans-serif; font-weight: 700;
    font-size: 14.5px; letter-spacing: .5px; margin-bottom: 14px;
  }
  .col-head .price { font-size: 19px; font-family: "Lato", sans-serif; }
  .options { list-style: none; font-size: 14.5px; line-height: 24px; }
  .options li::before { content: "• "; }
  .options .note { display: block; padding-left: 11px; line-height: 16px; margin-top: -4px; }

  .sandwich-band {
    position: absolute; left: 360px; top: 597px; width: 469px; height: 473px;
    background: var(--sky);
  }
  .omelet-frame {
    position: absolute; left: 49px; top: 557px; width: 422px; height: 553px;
    border: 3px solid var(--ink);
  }
  .section-head {
    position: absolute;
    font-family: "Josefin Sans", sans-serif; font-weight: 700;
    font-size: 21px; letter-spacing: 2px; line-height: 1;
  }
  .section-head small {
    display: block; font-family: "Josefin Sans", sans-serif; font-weight: 600;
    font-size: 11px; letter-spacing: .5px; margin-top: 2px;
  }
  .section-head .rule { margin-top: 24px; }

  .dish { position: absolute; }
  .dish__name {
    font-family: "Josefin Sans", sans-serif; font-weight: 700;
    font-size: 14px; letter-spacing: .8px;
  }
  .dish__desc { font-size: 12.5px; line-height: 16px; color: var(--ink-soft); margin-top: 6px; }
  .omelet { left: 86px; width: 225px; }
  .omelet .dish__desc { text-align: justify; }
  .omelet-price {
    position: absolute; left: 390px; font-weight: 700; font-size: 19px;
  }
  .sandwich { left: 524px; width: 250px; }
  .sandwich .dish__price { font-weight: 700; font-size: 27px; margin-bottom: 8px; }
</style>
</head>
<body>
  <section class="page page--cover">
    <div class="cover-mark"><span class="dot"></span>KETTLEWELL</div>
  </section>

  <section class="page page--menu">
    <header class="masthead">
      <div class="masthead__name">KETTLEWELL</div>
      <div class="masthead__section">BREAKFAST</div>
    </header>

    <div class="builder">
      <h2 class="builder__title">BUILD YOUR OWN BREAKFAST SANDWICH<span class="rule"></span></h2>
      <div class="builder__col builder__col--bread">
        <div class="col-head"><span>CHOOSE YOUR BREAD</span><span class="price">$2.50</span></div>
        <ul class="options">
          <li>Bagels (daily selection)</li>
          <li>Brioche Roll</li>
          <li>Brioche Toast</li>
          <li>Ciabatta Rolls</li>
          <li>Croissant (add <b>$1.00</b>)</li>
          <li>Gluten Free bagel<span class="note">(add <b>$1.00</b>)</span></li>
        </ul>
      </div>
      <div class="builder__col builder__col--cheese">
        <div class="col-head"><span>ADD CHEESE</span><span class="price">$1.00</span></div>
        <ul class="options">
          <li>American</li>
          <li>Cheddar</li>
          <li>Pepper Jack</li>
          <li>Swiss</li>
          <li>Cream Cheese</li>
          <li>Flavor Cream Cheese<span class="note">(add <b>$0.50</b>)</span></li>
        </ul>
      </div>
      <div class="builder__col builder__col--protein">
        <div class="col-head"><span>ADD PROTEIN</span><span class="price">$1.00</span></div>
        <ul class="options">
          <li>Bacon</li>
          <li>Egg</li>
          <li>Turkey Bacon</li>
          <li>Pork Roll</li>
          <li>Sausage</li>
          <li>Avocado</li>
        </ul>
      </div>
    </div>

    <div class="sandwich-band"></div>
    <div class="omelet-frame"></div>

    <h2 class="section-head" style="left:86px;top:597px;">OMELETS<small>SERVED WITH HOME FRIES OR FRUITS</small><span class="rule"></span></h2>

    <div class="dish omelet" style="top:684px;">
      <div class="dish__name">EGG WHITE OMELET</div>
      <p class="dish__desc">Marinated chicken breast and broccoli stuffed.</p>
    </div>
    <div class="omelet-price" style="top:680px;">$9.95</div>

    <div class="dish omelet" style="top:771px;">
      <div class="dish__name">VEGETABLE OMELET</div>
      <p class="dish__desc">Mushrooms, peppers, red onion, spinach, and cheddar cheese.</p>
    </div>
    <div class="omelet-price" style="top:767px;">$9.95</div>

    <div class="dish omelet" style="top:858px;">
      <div class="dish__name">CHICKEN OMELET</div>
      <p class="dish__desc">Marinated chicken breast, spinach, tomato, caramelized onions, and pepper jack cheese.</p>
    </div>
    <div class="omelet-price" style="top:854px;">$9.95</div>

    <div class="dish omelet" style="top:953px;">
      <div class="dish__name">SMOKED SALMON OMELET</div>
      <p class="dish__desc">Green onions, red peppers, cream cheese, and sliced smoked salmon stuffed inside an omelet.</p>
    </div>
    <div class="omelet-price" style="top:949px;">$11.95</div>

    <h2 class="section-head" style="left:524px;top:638px;">SANDWICH<small>SERVED WITH HOME FRIES OR FRUITS</small><span class="rule"></span></h2>

    <div class="dish sandwich" style="top:712px;">
      <div class="dish__price">$7.95</div>
      <div class="dish__name">EBLT</div>
      <p class="dish__desc">Fried egg, crispy bacon, arugula, tomato, and mayonnaise on brioche roll.</p>
    </div>
    <div class="dish sandwich" style="top:826px;">
      <div class="dish__price">$11.95</div>
      <div class="dish__name">SMOKED SALMON SANDWICH</div>
      <p class="dish__desc">Sliced smoked salmon, cream cheese, red onion, lettuce, and tomato between a soft toasted brioche roll.</p>
    </div>
    <div class="dish sandwich" style="top:952px;">
      <div class="dish__price">$13.95</div>
      <div class="dish__name">BREAKFAST BURGER</div>
      <p class="dish__desc">Angus Beef, sausage patty, cheddar cheese, caramelized onions, lettuce and tomato on toasted brioche roll.</p>
    </div>
  </section>
</body>
</html>
```